I already have a logo created by Quillory Makers that I'm very happy with. I need to spruce up my business card now. Its a double sided card with not much info on it, I like to keep it simple.
Front of card: name, phone # email address, web address. Tag Line "Outsourced Technology Solutions", under that it says Business Voice Services & Electronic Protection.
Rear of Card: Content written inside a "cloud" saying "Cloud Solutions" "Cloud Integrity"

Target Market(s)

Business to Business

Industry/Entity Type

Business

Contact Information for Business Card

We are in the technology field. Providing Telephone systems (hardware), SIP Trunks (dial tone/local/long distance/telephone #'s), LAN (Local Area Network)infrastructure cabling, Data Center solutions and Security Applications (Camera systems, Access Control systems,

Requirements
Must have
• Must have brevity
Should not have
• Clutter and/or too much information

```html
<!DOCTYPE html>
<html lang="en">
<head>
<meta charset="utf-8">
<title>Northvale Networks — Business Card</title>
<link rel="stylesheet" href="https://fonts.googleapis.com/css2?family=Open+Sans:ital,wght@0,400;0,600;1,400&display=swap">
<style>
  :root {
    --bg: #3a3a3c;
    --navy: #0f3478;
    --navy-deep: #0a2660;
    --navy-light: #1d4c9c;
    --paper: #ffffff;
    --grey-text: #7a7d82;
    --dark-text: #3d3f43;
    --rule: #c9ccd1;
  }
  * { box-sizing: border-box; margin: 0; padding: 0; }
  html, body { width: 1200px; height: 843px; overflow: hidden; }
  body {
    background: var(--bg);
    font-family: "Open Sans", Arial, sans-serif;
    position: relative;
  }
  .card {
    position: absolute;
    width: 620px;
    height: 354px;
    border-radius: 3px;
    overflow: hidden;
  }

  /* Back side */
  .card-back {
    left: 60px; top: 50px;
    background: linear-gradient(135deg, var(--navy-light) 0%, var(--navy) 50%, var(--navy-deep) 100%);
    color: var(--paper);
    display: flex; flex-direction: column; align-items: center; justify-content: center;
    text-align: center;
  }
  .card-back .brand { display: flex; align-items: center; gap: 12px; }
  .card-back .brand-mark { width: 22px; height: 22px; background: var(--paper); }
  .card-back .brand-name { font-size: 30px; font-weight: 600; color: var(--paper); }
  .card-back .tagline { margin-top: 6px; font-size: 17px; letter-spacing: 0.5px; color: #dfe6f3; border-top: 1px solid rgba(255,255,255,0.6); padding-top: 4px; }
  .card-back .services { margin-top: 34px; font-size: 21px; font-weight: 600; letter-spacing: 0.3px; }

  /* Front side */
  .card-front {
    left: 520px; top: 440px;
    background: var(--paper);
  }
  .contact { position: absolute; left: 40px; top: 96px; }
  .contact .name { font-size: 24px; font-weight: 600; color: var(--navy); }
  .contact .role { font-size: 16px; color: var(--grey-text); margin-top: 2px; }
  .contact ul { list-style: none; margin-top: 24px; }
  .contact li { display: flex; align-items: center; gap: 12px; font-size: 16px; color: var(--dark-text); margin-bottom: 8px; }
  .contact svg { width: 16px; height: 16px; fill: var(--navy); }

  .front-brand { position: absolute; right: 36px; top: 56px; text-align: left; }
  .front-brand .brand { display: flex; align-items: center; gap: 10px; }
  .front-brand .brand-mark { width: 18px; height: 18px; background: var(--navy); }
  .front-brand .brand-name { font-size: 22px; font-weight: 600; color: var(--navy); }
  .front-brand .tagline { font-size: 13px; color: var(--grey-text); margin-top: 3px; border-top: 1px solid var(--rule); padding-top: 3px; }
  .front-brand .services { font-size: 15px; font-style: italic; color: var(--dark-text); margin-top: 10px; line-height: 1.35; }

  .web-band {
    position: absolute; left: 0; right: 0; top: 258px; height: 38px;
    background: linear-gradient(90deg, var(--navy) 0%, var(--navy-light) 55%, var(--navy) 100%);
    color: var(--paper);
    font-size: 16px; letter-spacing: 6px;
    display: flex; align-items: center; padding-left: 40px;
  }
  .base-rule { position: absolute; left: 0; right: 0; top: 306px; height: 6px; background: var(--rule); }
</style>
</head>
<body>

  <section class="card card-back" aria-label="Card back">
    <div class="brand">
      <span class="brand-mark"></span>
      <span class="brand-name">Northvale Networks, LLC</span>
    </div>
    <p class="tagline">Outsourced Technology Solutions</p>
    <p class="services">Cloud Solutions &nbsp;|&nbsp; Cloud Integrity</p>
  </section>

  <section class="card card-front" aria-label="Card front">
    <div class="contact">
      <p class="name">Marin Keller</p>
      <p class="role">President</p>
      <ul>
        <li>
          <svg viewBox="0 0 24 24" aria-hidden="true"><path d="M6.6 10.8a15.1 15.1 0 0 0 6.6 6.6l2.2-2.2a1 1 0 0 1 1-.25 11.4 11.4 0 0 0 3.6.57 1 1 0 0 1 1 1V20a1 1 0 0 1-1 1A17 17 0 0 1 3 4a1 1 0 0 1 1-1h3.5a1 1 0 0 1 1 1c0 1.25.2 2.45.57 3.57a1 1 0 0 1-.25 1z"/></svg>
          555 0142 7788
        </li>
        <li>
          <svg viewBox="0 0 24 24" aria-hidden="true"><path d="M2 5h20v14H2z M2 5l10 8 10-8" fill="none" stroke="#0f3478" stroke-width="2"/></svg>
          marin@northvale.net
        </li>
      </ul>
    </div>

    <div class="front-brand">
      <div class="brand">
        <span class="brand-mark"></span>
        <span class="brand-name">Northvale Networks, LLC</span>
      </div>
      <p class="tagline">Outsourced Technology Solutions</p>
      <p class="services">Business Voice Services &amp;<br>Electronic Protection</p>
    </div>

    <div class="web-band">www.northvale.net</div>
    <div class="base-rule"></div>
  </section>

</body>
</html>
```